KT Fenwick's Brochure - Brevanta Solutions

Hello,
We have an example of very simple brochure (attached below). We would like you to make it better. More sophisticated. More professional looking. All of the info in the document needs to go in the brochure.
Please let me know if you can execute. I will be happy to send over photos, logos etc, once I know.

```html
<!DOCTYPE html>
<html lang="en">
<head>
<meta charset="utf-8">
<title>KT Fenwick's Brochure – Brevanta Solutions</title>
<link href="https://fonts.googleapis.com/css2?family=Montserrat:wght@500;700;800;900&family=Oswald:wght@500&display=swap" rel="stylesheet">
<style>
  :root{
    --navy:#1f3a73;
    --navy-deep:#163366;
    --band:#183c7c;
    --paper:#f4f5f7;
    --stage:#e4e5e8;
    --white:#ffffff;
    --ink:#2a3550;
  }
  *{box-sizing:border-box;margin:0;padding:0}
  html,body{width:1200px;height:953px;overflow:hidden;background:var(--stage)}
  body{font-family:"Montserrat",Arial,sans-serif;position:relative}
  .spread{position:absolute;left:30px;top:94px;width:1140px;height:765px;display:flex}
  .page{position:relative;width:570px;height:765px;overflow:hidden}
  .page--left{background:var(--band)}
  .page--right{background:var(--paper)}

  .photo{position:absolute}
  .photo--office{left:0;top:0;width:570px;height:288px;background:linear-gradient(180deg,#3f74c4 0%,#8fb2de 45%,#c9d6e3 70%,#8a9163 88%,#a58a5e 100%)}
  .band{position:absolute;left:0;top:288px;width:570px;height:46px;background:var(--band)}
  .photo--clinic{left:0;top:334px;width:570px;height:431px;background:linear-gradient(160deg,#2f69c6 0%,#3a6bb8 40%,#3b4f7e 70%,#2a3a66 100%)}
  .photo--tower{left:0;top:0;width:305px;height:410px;background:linear-gradient(180deg,#6f9fdb 0%,#a9b9cc 40%,#a4685a 70%,#8c8f96 100%)}
  .photo--highrise{left:305px;top:340px;width:265px;height:425px;background:linear-gradient(180deg,#6d9ee2 0%,#c8cdd2 45%,#b99a74 80%,#6b8a5a 100%)}

  .logo{position:absolute;display:flex;align-items:center;gap:5px;font-family:"Oswald",Arial,sans-serif;font-weight:500;letter-spacing:1px;font-size:17px}
  .logo__mark{width:8px;height:8px;background:currentColor}
  .logo--left{left:28px;top:42px;color:var(--white)}
  .logo--right{left:32px;top:50px;color:var(--white)}
  .logo--foot{left:44px;top:718px;color:var(--navy);font-size:14px}

  .title{position:absolute;font-weight:900;line-height:1.12}
  .title--left{right:45px;top:42px;text-align:right;font-size:33px;color:var(--navy-deep)}
  .title--left .lead{color:var(--white)}
  .title--right{left:150px;top:46px;font-size:33px;color:var(--navy-deep);white-space:nowrap}
  .title--right .lead{color:var(--white)}

  .tag{position:absolute;background:var(--navy);color:var(--white);font-family:"Oswald",Arial,sans-serif;font-weight:500;font-size:12px;letter-spacing:1.6px;display:flex;align-items:center;white-space:nowrap}
  .tag::after{content:"";position:absolute;inset:-6px -6px -6px 6px;border:1px solid rgba(255,255,255,.7);pointer-events:none}
  .tag--office{left:0;top:212px;width:250px;height:32px;padding-left:12px}
  .tag--clinic{right:0;top:442px;height:36px;padding:0 14px 0 16px}
  .tag--clinic::after{inset:-6px 0 -6px -6px}
  .tag--tower{left:240px;top:158px;width:205px;height:34px;justify-content:center}
  .tag--highrise{left:372px;top:318px;width:186px;height:32px;justify-content:center}

  .veil{position:absolute;background:rgba(40,80,150,.45)}
  .veil--a{left:272px;top:312px;width:78px;height:125px}
  .veil--b{left:262px;top:318px;width:60px;height:105px;background:none;border:1px solid rgba(255,255,255,.8)}

  .copy{position:absolute}
  .copy__intro{font-weight:800;font-size:9.5px;letter-spacing:.9px;line-height:1.95;text-transform:uppercase}
  .copy__list{list-style:none;margin-top:14px}
  .copy__list li{position:relative;padding-left:19px;font-size:9.6px;letter-spacing:.6px;line-height:1.6;font-weight:500}
  .copy__list li::before{content:"";position:absolute;left:0;top:4px;width:7px;height:7px;background:currentColor}
  .copy--left{left:64px;top:412px;width:300px;color:var(--white)}
  .copy--left .copy__list li{margin-bottom:13px}
  .copy--right{left:62px;top:444px;width:236px;color:var(--ink)}
  .copy--right .copy__intro{color:var(--navy)}
  .copy--right .copy__list{margin-top:10px}
  .copy--right .copy__list li{margin-bottom:8px;font-size:9px;letter-spacing:.5px}
  .copy--right .copy__list li::before{background:var(--navy)}

  .folio{position:absolute;font-weight:700;font-style:italic;font-size:17px}
  .folio--3{left:510px;top:718px;color:var(--white);padding-left:10px;border-left:1px solid rgba(255,255,255,.8)}
  .folio--4{left:145px;top:720px;color:var(--navy);padding-left:8px;border-left:2px solid var(--navy)}
</style>
</head>
<body>
<main class="spread">
  <section class="page page--left">
    <div class="photo photo--office" role="img" aria-label="Photograph of a glass-clad office headquarters with lawn and flag under a blue sky"></div>
    <div class="band"></div>
    <div class="photo photo--clinic" role="img" aria-label="Blue-toned photograph of a brick medical centre with ribbon windows and snowy parking"></div>
    <div class="logo logo--left"><span class="logo__mark"></span>KT FENWICK</div>
    <h1 class="title title--left"><span class="lead">Brevanta</span><br>Ribbon Wall &amp;<br>Storefront</h1>
    <div class="tag tag--office">SUMMIT FEDERAL COLORADO SPRINGS</div>
    <div class="tag tag--clinic">RIDGELINE HEALTH LONGMONT</div>
    <div class="copy copy--left">
      <p class="copy__intro">Designed for quality and fast installation. This 2" by 4 1/2" system offers the following benefits:</p>
      <ul class="copy__list">
        <li>Installed from the interior or exterior</li>
        <li>12 psi water rating</li>
        <li>Higher thermal performance due to thermal strut</li>
        <li>Two color option (interior/exterior)</li>
        <li>Larger panes of glass to improve views</li>
        <li>Shipped on metal racks or wood crates</li>
      </ul>
    </div>
    <div class="folio folio--3">3</div>
  </section>

  <section class="page page--right">
    <div class="photo photo--tower" role="img" aria-label="Photograph of a brick and glass residential high-rise on a city corner"></div>
    <div class="photo photo--highrise" role="img" aria-label="Aerial photograph of a tall downtown apartment tower with street below"></div>
    <div class="veil veil--a"></div>
    <div class="veil veil--b"></div>
    <div class="logo logo--right"><span class="logo__mark"></span>KT FENWICK</div>
    <h2 class="title title--right"><span class="lead">Brevanta</span> Window Wall</h2>
    <div class="tag tag--tower">12TH &amp; ALDER DENVER CO</div>
    <div class="tag tag--highrise">THE HARLOW DENVER CO</div>
    <div class="copy copy--right">
      <p class="copy__intro">Designed by installers for an efficient installaton with large vision areas. This 6" deep window system offers the following benefits:</p>
      <ul class="copy__list">
        <li>Punched openings or window wall runs.</li>
        <li>Installed from the interior using a receptor system.</li>
        <li>Metal slab covers.</li>
        <li>Trim clips are attached.</li>
        <li>Shipped on metal racks or wood crates.</li>
      </ul>
    </div>
    <div class="logo logo--foot"><span class="logo__mark"></span>KT FENWICK</div>
    <div class="folio folio--4">4</div>
  </section>
</main>
</body>
</html>
```